Brochure for a civil enineering company in A4 format

I need a brochure design for our company VELTA Engineering S.r.l.. We are an engineering consultant company. Our main clients are from the infrastructure industry (geotechnical and underground sectors mainly).
We are looking for a 2 pages (4 faces) fold out design with a glued pocket where we can put individual data sheets.
I need A4 format pages.

Target Market(s)

We are an engineering consultant company. Our main clients are from the infrastructure industry (geotechnical and underground sectors mainly).

Industry/Entity Type

Civil Engineer

Font styles to use
Sans Serif

Requirements
Must have
• Overall: 2 pages in A4 format
Essential style. Bright and modern appearance.
Glued pocket
Logo integrated in a picture on the pocket where I would like to insert a slogan (… velta engineering … reliable solutions …)
Attached are selected images which the designer can use and edit at their own discretion.
Some advice in the following (anyway designers are free to provide their solutions):
Outer sheets:
Front page with name, logo. It could be nice to have the “m” of the logo integrated in a pictures, also a modified picture (I mean modify one of the attached pictures) so to create a general image and do not tie the cover to a specific job.
Back page: offices address and contact email address. Nice to have one space for a slogan.
Inner sheet: text that I upload in the file “inside-sheets”, possibly with pictures on each sheet. In the right faces insert the glued pocket. On this pages insert the section OUR EXPERIENCE ….with a space for a picture of our team.
Nice to have
• Clean and essential design.
Pictures choosing from the atteched ones. Pictures could be modified in a very light manner to make them a general idea of the work ( I mean geotechnical world) without to be immediately linked to a specific site.
Should not have
• excessive frills

```html
<!DOCTYPE html>
<html lang="it">
<head>
<meta charset="utf-8">
<title>VELTA Engineering – Brochure</title>
<link rel="stylesheet" href="https://fonts.googleapis.com/css2?family=Arimo:wght@400;700&family=IBM+Plex+Mono:wght@400&display=swap">
<style>
:root{
  --bg:#e6e6e6;
  --paper:#ffffff;
  --ink:#1b1b1b;
  --text:#333333;
  --muted:#555555;
  --band:#d8d8d8;
  --avatar:#b9b9b9;
  --dash:#9a9a9a;
}
*{margin:0;padding:0;box-sizing:border-box}
html,body{width:1200px;height:2452px;overflow:hidden;background:var(--bg)}
body{position:relative;font-family:"Arimo",Arial,sans-serif;color:var(--text)}
.abs{position:absolute}
.brand{font-family:"Arimo",Arial,sans-serif;font-weight:700;color:var(--ink);letter-spacing:-1px;line-height:1}
.slogan{font-family:"IBM Plex Mono",monospace;font-size:9px;letter-spacing:2.4px;color:var(--ink);text-transform:uppercase}
.photo{position:absolute}

/* cover */
.cover{position:absolute;left:289px;top:60px;width:622px;height:880px;background:var(--paper);box-shadow:0 12px 30px rgba(0,0,0,.18)}
.cover .brand{position:absolute;left:56px;top:206px;font-size:44px}
.cover .slogan{position:absolute;right:30px;top:222px}
.cover .url{position:absolute;right:30px;bottom:40px;font-size:9px;color:var(--ink)}

/* spread */
.spread{position:absolute;left:114px;top:1000px;width:973px;height:1386px;background:var(--paper)}
.fold{position:absolute;left:486px;top:0;width:1px;height:100%;background:#eee}
.address{position:absolute;left:160px;top:52px;width:180px;text-align:center;font-size:9.5px;line-height:1.15;color:var(--ink)}
.address b{display:block;font-size:10px;margin-top:8px}
.address .web{margin-top:10px}
.spread .brand.main{position:absolute;left:516px;top:82px;font-size:40px}
.spread .slogan.main{position:absolute;right:32px;top:175px}
.band{position:absolute;left:0;top:690px;width:973px;height:8px;background:var(--band)}
.pocket{position:absolute;left:516px;top:726px;width:428px;height:148px;border:1px dashed var(--dash);border-radius:8px}

.copy{position:absolute;font-size:8.3px;line-height:1.22;text-align:justify;color:var(--text)}
.copy h2{font-size:9.6px;font-weight:700;color:var(--ink);margin:0 0 4px}
.copy p{margin:0 0 4px}
.copy ul{list-style:none;margin:0 0 0 12px}
.copy li{margin:0 0 3px;padding-left:6px;text-indent:-6px}
.copy li::before{content:"• "}
.left-copy{left:30px;top:895px;width:428px}
.right-copy{left:516px;top:895px;width:428px}
.gap{height:14px}
.founder{overflow:hidden;margin-bottom:8px}
.avatar{float:left;width:44px;height:44px;border-radius:50%;background:var(--avatar);border:2px solid #8e8e8e;margin:2px 8px 2px 2px}
.footer-brand{position:absolute;left:30px;top:1330px;font-size:18px}
.footer-url{position:absolute;right:30px;top:1338px;font-size:8px;color:var(--muted)}
</style>
</head>
<body>

<!-- Front cover -->
<section class="cover">
  <div class="brand">velta</div>
  <div class="slogan">Velta ingegneria , soluzioni affidabili</div>
  <div class="photo" role="img" aria-label="Cantiere interno di edificio in demolizione" style="left:90px;top:250px;width:177px;height:180px;background:linear-gradient(160deg,#7b6e5c,#4c4338)"></div>
  <div class="photo" role="img" aria-label="Gru che solleva la testa di una fresa TBM" style="left:267px;top:250px;width:177px;height:180px;background:linear-gradient(180deg,#4e8fc7,#9fb3c4 60%,#8a7d6e)"></div>
  <div class="photo" role="img" aria-label="Escavatore in galleria in costruzione" style="left:444px;top:250px;width:178px;height:180px;background:linear-gradient(160deg,#6f6455,#c07a3c 70%,#514739)"></div>
  <div class="photo" role="img" aria-label="Stazione ferroviaria con cantiere" style="left:90px;top:430px;width:177px;height:180px;background:linear-gradient(180deg,#c9d4de,#a7988a 50%,#7a6b5c)"></div>
  <div class="photo" role="img" aria-label="Interno di galleria in bianco e nero" style="left:267px;top:430px;width:177px;height:180px;background:radial-gradient(circle at 60% 50%,#8c8c8c,#222 70%)"></div>
  <div class="photo" role="img" aria-label="Scavo a cielo aperto in area urbana" style="left:444px;top:430px;width:178px;height:180px;background:linear-gradient(180deg,#b9c2c9,#a99e90 45%,#8e8476)"></div>
  <div class="photo" role="img" aria-label="Pozzo circolare di scavo con armature" style="left:90px;top:610px;width:177px;height:180px;background:radial-gradient(circle,#5a544b,#9c9385 70%)"></div>
  <div class="photo" role="img" aria-label="Viadotto in paesaggio montano" style="left:267px;top:610px;width:177px;height:180px;background:linear-gradient(180deg,#7aa6d4,#9db5c7 40%,#6f7a5e 60%,#8b6f5c)"></div>
  <div class="photo" role="img" aria-label="Imbocco di galleria in scavo" style="left:444px;top:610px;width:178px;height:180px;background:linear-gradient(160deg,#a79c8a,#6b6154)"></div>
  <div class="url">www.veltaengineering.org</div>
</section>

<!-- Open spread -->
<section class="spread">
  <div class="fold"></div>

  <div class="address">
    <b style="margin-top:0">Milano</b>
    Via Fiori, 14<br>20121 Milano - IT<br>+39 02 44556677
    <b>Riva TN</b>
    Via San Marco, 9<br>38066 Riva TN - IT<br>+39 02 44556677
    <div class="web">www.veltaengineering.org<br>velta_info@veltaengineering.org</div>
  </div>

  <div class="brand main">velta</div>
  <div class="slogan main">Velta ingegneria , soluzioni affidabili</div>

  <!-- photo grid, 6 x 3 -->
  <div class="photo" role="img" aria-label="Galleria illuminata con sfere" style="left:0;top:196px;width:162px;height:166px;background:linear-gradient(160deg,#7d6a54,#c8b8a2 60%,#5b4e40)"></div>
  <div class="photo" role="img" aria-label="Fondazioni in calcestruzzo su collina" style="left:162px;top:196px;width:162px;height:166px;background:linear-gradient(180deg,#8c9a74,#b7aa97 50%,#938a7e)"></div>
  <div class="photo" role="img" aria-label="Doppia galleria notturna" style="left:324px;top:196px;width:162px;height:166px;background:linear-gradient(180deg,#4a4d6e,#2f3046)"></div>
  <div class="photo" role="img" aria-label="Cantiere interno di edificio" style="left:486px;top:196px;width:162px;height:166px;background:linear-gradient(160deg,#7b6e5c,#4c4338)"></div>
  <div class="photo" role="img" aria-label="Gru che solleva la testa di una fresa TBM" style="left:648px;top:196px;width:162px;height:166px;background:linear-gradient(180deg,#4e8fc7,#9fb3c4 60%,#8a7d6e)"></div>
  <div class="photo" role="img" aria-label="Escavatore in galleria" style="left:810px;top:196px;width:163px;height:166px;background:linear-gradient(160deg,#6f6455,#c07a3c 70%,#514739)"></div>

  <div class="photo" role="img" aria-label="Scavo urbano con edifici" style="left:0;top:362px;width:162px;height:166px;background:linear-gradient(180deg,#b6c3d0,#a3968a 45%,#8f8479)"></div>
  <div class="photo" role="img" aria-label="Interno di galleria scuro" style="left:162px;top:362px;width:162px;height:166px;background:radial-gradient(circle at 50% 30%,#9aa0a0,#2e2a25 70%)"></div>
  <div class="photo" role="img" aria-label="Vista aerea di cantiere" style="left:324px;top:362px;width:162px;height:166px;background:linear-gradient(160deg,#6f7a5e,#9c938a 60%,#c6987c)"></div>
  <div class="photo" role="img" aria-label="Stazione ferroviaria con cantiere" style="left:486px;top:362px;width:162px;height:166px;background:linear-gradient(180deg,#c9d4de,#a7988a 50%,#7a6b5c)"></div>
  <div class="photo" role="img" aria-label="Galleria in bianco e nero" style="left:648px;top:362px;width:162px;height:166px;background:radial-gradient(circle at 60% 50%,#8c8c8c,#222 70%)"></div>
  <div class="photo" role="img" aria-label="Scavo a cielo aperto" style="left:810px;top:362px;width:163px;height:166px;background:linear-gradient(180deg,#b9c2c9,#a99e90 45%,#8e8476)"></div>

  <div class="photo" role="img" aria-label="Scavo profondo con paratie" style="left:0;top:528px;width:162px;height:162px;background:linear-gradient(160deg,#8d8272,#5d5448)"></div>
  <div class="photo" role="img" aria-label="Gru davanti a due imbocchi di galleria" style="left:162px;top:528px;width:162px;height:162px;background:linear-gradient(180deg,#c7d3dd,#a79b88 50%,#6a6055)"></div>
  <div class="photo" role="img" aria-label="Galleria ad arco illuminata" style="left:324px;top:528px;width:162px;height:162px;background:radial-gradient(circle at 50% 35%,#a9a294,#3b352d 70%)"></div>
  <div class="photo" role="img" aria-label="Pozzo circolare di scavo" style="left:486px;top:528px;width:162px;height:162px;background:radial-gradient(circle,#5a544b,#9c9385 70%)"></div>
  <div class="photo" role="img" aria-label="Viadotto in paesaggio montano" style="left:648px;top:528px;width:162px;height:162px;background:linear-gradient(180deg,#7aa6d4,#9db5c7 40%,#6f7a5e 60%,#8b6f5c)"></div>
  <div class="photo" role="img" aria-label="Imbocco di galleria in scavo" style="left:810px;top:528px;width:163px;height:162px;background:linear-gradient(160deg,#a79c8a,#6b6154)"></div>

  <div class="band"></div>

  <div class="photo" role="img" aria-label="Cantiere costiero con galleria" style="left:0;top:698px;width:162px;height:176px;background:linear-gradient(180deg,#c5cfd8,#8b9a78 45%,#b8a48e)"></div>
  <div class="photo" role="img" aria-label="Vista aerea di cantiere con armature" style="left:162px;top:698px;width:162px;height:176px;background:linear-gradient(160deg,#8a7e70,#5f564b)"></div>
  <div class="photo" role="img" aria-label="Fresa TBM in cantiere" style="left:324px;top:698px;width:162px;height:176px;background:linear-gradient(180deg,#c3c8cc,#a09582 60%,#7c7060)"></div>

  <div class="pocket" aria-label="Tasca incollata per schede tecniche"></div>

  <div class="copy left-copy">
    <h2>LA NOSTRA AZIENDA</h2>
    <p>VELTA Engineering S.r.l. offre servizi di consulenza tecnica, contrattuale e strategica ai principali attori nei settori delle scienze geologiche, dell’ingegneria geotecnica e dell’ingegneria idraulica. Lavoriamo per mitigare il rischio e ridurre l’incertezza, con flessibilità nella ricerca della soluzione ottimale contribuendo ad aumentare la redditività del progetto.</p>
    <p>VELTA Engineering S.r.l. è una società indipendente che nasce nel luglio 2020 dall’associazione di un gruppo di professionisti che hanno messo a fattor comune la reciproca esperienza maturata in oltre trent’anni di attività come progettisti e consulenti nel settore delle grandi opere di ingegneria civile lavorando come Direttori Tecnici di Main Engineering Companies and as Freelancers.</p>
    <p>VELTA Engineering Srl. vuole unire l’esperienza dei Fondatori e delle figure chiave con l’entusiasmo di chi intraprende una nuova attività, per dare vita ad una nuova realtà che si pone come obbiettivo principale il design of infrastructures that sono sicuri, sostenibili ed economici.</p>
    <p>Ciascuno dei nostri progetti rappresenta un impegno a lungo termine, crediamo nel fornire sicurezza, affidabilità, soluzioni innovative e sostenibili. Questa è e sarà la nostra caratteristica distintiva.</p>
    <div class="gap"></div>
    <h2>I NOSTRI SERVIZI</h2>
    <p>Progettazione e consulenza specialistica nel campo della geologia, dell’ingegneria geotecnica, delle opere sotterranee e dell’ingegneria idraulica.</p>
    <p>Aiutiamo i nostri clienti a risolvere problemi di natura progettuale, contrattuale e costruttiva che possono nascere nell’intera vita del progetto portando la nostra esperienza all’interno delle loro organizzazioni, migliorando la qualità dei loro servizi di ingegneria, ottimizzando i loro progetti, proponendo nuove idee e soluzioni, rafforzando i loro approcci...</p>
    <p>VELTA Engineering è in grado di fornire la propria assistenza nell’intero iter procedurale, dalla fase di indagine preliminare e di analisi di fattibilità fino alla progettazione costruttiva e all’assistenza tecnica in fase realizzativa. La specializzazione e l’esperienza accumulate nelle discipline della geologia, dell’ingegneria geotecnica e del sottosuolo e dell’idraulica ci permette di massimizzare la nostra efficacia quando sia necessario:</p>
    <ul>
      <li>far fronte a situazioni di emergenza anche su progetti in fase di sviluppo avanzato garantendo l’immediata focalizzazione delle problematiche di progetto e garantendo il risultato finale atteso (in termini di qualità, tempistiche e costi…)</li>
      <li>fornire “second opinion” di elevato valore tecnico ed amministrativo in occasione di problematiche progettuali e costruttive e dispute legali</li>
      <li>analizzare in tempi brevi progetti svolti da terzi individuandone le “criticità”, verificandone la cantierabilità e la validità tecnico economica.</li>
      <li>ottimizzare i progetti redatti da terzi implementandone il contenuto e massimizzando l’efficacia economica degli investimenti.</li>
    </ul>
  </div>

  <div class="copy right-copy">
    <h2>LA NOSTRA COMPETENZA ED ESPERIENZA</h2>
    <p>La società nasce dall’associazione di un gruppo di professionisti, con indiscusse competenze ed affidabilità, con esperienza maturata in oltre trent’anni di attività come progettisti e consulenti nel settore delle grandi opere di ingegneria civile; geologia, ingegneria geotecnica ed idraulica ed opere sotterranee sono il “core” delle loro competenze ….</p>
    <p>I soci fondatori sono:</p>
    <div class="founder"><div class="avatar" role="img" aria-label="Ritratto socio fondatore"></div>Lucia. Già Direttore Tecnico e Socio di SORTA Srl, nel periodo di sua permanenza fino al dicembre 2018, ha per essa firmato tutti i progetti nel campo delle opere sotterranee e la maggior parte di quelli di ingegneria geotecnica. Da gennaio 2019 è Direttore Tecnico di ALDEG. Può vantare più di 150 gallerie naturali, e numerosi progetti ed assistenze tecniche nel campo delle strutture geotecniche, delle sistemazioni idrogeologiche e dei versanti e delle opere di protezione ambientale. Negli ultimi dieci anni è stato responsabile di attività di assistenza tecnica, per imprese di costruzione, di opere il cui valore supera i 440 Mio EUR e di servizi di progettazione definitiva e/ o esecutiva per opere il cui valore supera i 1.400 Mio EUR. Ha svolto attività di verifica e validazione, in Italia ed all’estero, di numerosi progetti il cui valore complessivo supera i 3.400 Mio EUR.</div>
    <div class="founder"><div class="avatar" role="img" aria-label="Ritratto socio fondatore"></div>Marco 30 anni di esperienza professionale. Coinvolto in più di 150 gallerie naturali con lunghezza complessiva superiore a 360 km. Numerosi progetti ed attività di assistenza tecnica nel campo delle strutture, delle sistemazioni idrogeologiche e dei versanti e delle opere di protezione ambientale. Negli ultimi dieci anni responsabile di attività di assistenza tecnica in corso d’opera, per imprese di costruzione, di opere il cui valore supera i 440 Mio EUR e di servizi di progettazione definitiva o esecutiva per opere il cui valore supera i 1.400 Mio EUR. Ha svolto attività di verifica ai fini della validazione, in Italia ed all’estero, di numerosi progetti il cui valore complessivo supera i 3.400 Mio EUR.</div>
    <div class="founder"><div class="avatar" role="img" aria-label="Ritratto socio fondatore"></div>Elena 30 anni di esperienza professionale. Coinvolta in più di 150 gallerie naturali con lunghezza complessiva superiore a 360 km. Numerosi progetti ed attività di assistenza tecnica nel campo delle strutture, delle sistemazioni idrogeologiche e dei versanti e delle opere di protezione ambientale. Negli ultimi dieci anni responsabile di attività di assistenza tecnica in corso d’opera, per imprese di costruzione, di opere il cui valore supera i 440 Mio EUR e di servizi di progettazione definitiva o esecutiva per opere il cui valore supera i 1.400 Mio EUR. Ha svolto attività di verifica ai fini della validazione, in Italia ed all’estero, di numerosi progetti il cui valore complessivo supera i 3.400 Mio EUR.</div>
    <div class="founder"><div class="avatar" role="img" aria-label="Ritratto socio fondatore"></div>Paolo 30 anni di esperienza professionale. Coinvolto in più di 150 gallerie naturali con lunghezza complessiva superiore a 360 km. Numerosi progetti ed attività di assistenza tecnica nel campo delle strutture, delle sistemazioni idrogeologiche e dei versanti e delle opere di protezione ambientale. Negli ultimi dieci anni responsabile di attività di assistenza tecnica in corso d’opera, per imprese di costruzione, di opere il cui valore supera i 440 Mio EUR e di servizi di progettazione definitiva o esecutiva per opere il cui valore supera i 1.400 Mio EUR. Ha svolto attività di verifica ai fini della validazione, in Italia ed all’estero, di numerosi progetti il cui valore complessivo supera i 3.400 Mio EUR.</div>
  </div>

  <div class="brand footer-brand">velta</div>
  <div class="footer-url">www.veltaengineering.org</div>
</section>

</body>
</html>
```